Need Business Card for our Real Estate Business with Sales Executive's Picture

PANTONE 484 C ( RED)

PANTONE 2766 C ( BLUE

Industry/Entity Type

Real Estate

Contact Information for Business Card

Name, Mobile, email, & picture of Person
Agency Phone, address, Web address

Requirements
Must have
• Our Logo Colours, Agent Picture,

```html
<!DOCTYPE html>
<html lang="en">
<head>
<meta charset="utf-8">
<title>Veldra Real Estate – Business Card</title>
<link rel="stylesheet" href="https://fonts.googleapis.com/css2?family=Open+Sans:wght@400;600;700&display=swap">
<style>
  :root {
    --navy: #172a5e;
    --navy-deep: #121f4a;
    --red: #a3302a;
    --paper: #ffffff;
    --page: #e6e6e6;
    --faint: #eef0f4;
    --photo-light: #e9e6e2;
    --photo-dark: #2a3d78;
  }
  * { box-sizing: border-box; margin: 0; padding: 0; }
  html, body { width: 1200px; height: 852px; overflow: hidden; }
  body {
    background: var(--page);
    font-family: "Open Sans", Arial, sans-serif;
    position: relative;
  }
  .card {
    position: absolute;
    top: 276px;
    width: 520px;
    height: 300px;
    border-radius: 22px;
    overflow: hidden;
    box-shadow: 0 6px 16px rgba(0,0,0,.18);
  }
  .card--front { left: 60px; background: var(--navy); color: var(--paper); }
  .card--back { left: 620px; background: var(--paper); color: var(--navy); }

  /* brand wordmark */
  .brand { position: absolute; display: flex; align-items: center; gap: 10px; }
  .brand__square { width: 12px; height: 12px; background: var(--red); flex: none; }
  .brand__text { font-weight: 600; letter-spacing: .12em; line-height: 1; }
  .brand__name { display: block; }
  .brand__sub { display: block; font-size: .32em; letter-spacing: .3em; margin-top: 6px; text-align: center; }

  .card--front .brand { left: 0; right: 0; top: 92px; justify-content: center; }
  .card--front .brand__text { font-size: 46px; color: var(--paper); }
  .front__rule { position: absolute; left: 130px; right: 130px; top: 176px; height: 1px; background: rgba(255,255,255,.7); }
  .front__web { position: absolute; left: 0; right: 0; bottom: 34px; text-align: center; font-size: 14px; letter-spacing: .03em; }
  .front__accent { position: absolute; bottom: 42px; width: 52px; height: 2px; background: var(--red); }
  .front__accent--left { left: 82px; transform: rotate(-12deg); }
  .front__accent--right { right: 82px; transform: rotate(-12deg); }
  .front__accent--top { right: 60px; bottom: auto; top: 192px; transform: rotate(-12deg); }

  /* back side */
  .card--back .brand { left: 250px; top: 30px; }
  .card--back .brand__text { font-size: 34px; color: var(--navy); }
  .back__rule { position: absolute; left: 230px; top: 88px; width: 240px; height: 1px; background: var(--navy); }
  .back__faint { position: absolute; right: 40px; top: 96px; width: 110px; height: 110px; background: var(--faint); border-radius: 4px; }

  .person { position: absolute; left: 38px; top: 112px; }
  .person__name { font-size: 19px; font-weight: 700; color: var(--navy); }
  .person__role { font-size: 13px; color: var(--red); margin-top: 2px; }

  .edge-dot { position: absolute; left: -18px; top: 158px; width: 36px; height: 36px; border-radius: 50%; background: var(--red); }

  .portrait {
    position: absolute; left: 148px; top: 150px; width: 200px; height: 150px;
    background: linear-gradient(180deg, var(--photo-light) 0%, var(--photo-light) 35%, var(--photo-dark) 100%);
  }

  .contact { position: absolute; left: 340px; top: 112px; font-size: 12px; line-height: 1.45; color: var(--navy); }
  .contact__address { margin-bottom: 6px; }
  .contact__row { display: flex; align-items: center; gap: 8px; }
  .contact__icon { width: 11px; height: 11px; flex: none; }

  .web-tab {
    position: absolute; right: 0; bottom: 0; width: 180px; height: 58px;
    background: var(--navy); border-top-left-radius: 18px;
    color: var(--paper); font-size: 13px; display: flex; align-items: center; justify-content: center;
  }
  .web-tab__notch { position: absolute; left: 334px; bottom: 52px; width: 14px; height: 8px; background: var(--red); border-radius: 4px 0 0 0; }
</style>
</head>
<body>

  <section class="card card--front" aria-label="Card front">
    <div class="brand">
      <span class="brand__square"></span>
      <span class="brand__text"><span class="brand__name">VELDRA</span><span class="brand__sub">REAL ESTATE</span></span>
    </div>
    <div class="front__rule"></div>
    <span class="front__accent front__accent--top"></span>
    <span class="front__accent front__accent--left"></span>
    <span class="front__accent front__accent--right"></span>
    <p class="front__web">www.veldrarealty.com</p>
  </section>

  <section class="card card--back" aria-label="Card back">
    <div class="back__faint"></div>
    <div class="brand">
      <span class="brand__square"></span>
      <span class="brand__text"><span class="brand__name">VELDRA</span><span class="brand__sub">REAL ESTATE</span></span>
    </div>
    <div class="back__rule"></div>

    <div class="person">
      <p class="person__name">Marissa Holt</p>
      <p class="person__role">Managing Director</p>
    </div>
    <span class="edge-dot"></span>

    <div class="portrait" role="img" aria-label="Portrait photo of the agent in a navy suit"></div>

    <div class="contact">
      <p class="contact__address">418 Crestline Ave #2207,<br>Arvada, CO 80004</p>
      <p class="contact__row">
        <svg class="contact__icon" viewBox="0 0 12 12"><rect x="3" y="0.5" width="6" height="11" rx="1.2" fill="var(--red)"/><rect x="4.2" y="2" width="3.6" height="6" fill="#fff"/></svg>
        555.210.3847
      </p>
      <p class="contact__row">
        <svg class="contact__icon" viewBox="0 0 12 12"><path d="M1 4 Q6 0 11 4 L9.5 5.5 L8 4.5 L4 4.5 L2.5 5.5 Z" fill="var(--red)"/><rect x="2" y="6" width="8" height="5" rx="1" fill="var(--red)"/></svg>
        555-318-6402
      </p>
      <p class="contact__row">
        <svg class="contact__icon" viewBox="0 0 12 12"><rect x="0.5" y="2.5" width="11" height="7" fill="var(--red)"/><path d="M0.5 2.5 L6 7 L11.5 2.5" stroke="#fff" stroke-width="1" fill="none"/></svg>
        mholt@veldrarealty.com
      </p>
    </div>

    <span class="web-tab__notch"></span>
    <div class="web-tab">www.veldrarealty.com</div>
  </section>

</body>
</html>
```